Business card for utility of the future

I need a business card template designed for brookvane. We provide sustainable water, energy and waste services to homes.

The card should include name, position, email address, phone number, website and our logo (attached). I would like it to convey professionalism and creativity.

Target Market(s)

Homeowners, investors, corporate partners.

Industry/Entity Type

Utility

Contact Information for Business Card

The card should include name, position, email address, phone number, website and our logo (attached).

```html
<!DOCTYPE html>
<html lang="en">
<head>
<meta charset="utf-8">
<title>brookvane business card</title>
<link href="https://fonts.googleapis.com/css2?family=Cabin:wght@600;700&display=swap" rel="stylesheet">
<style>
  :root {
    --page: #ffffff;
    --frame: #c8c8c8;
    --brand-green: #4aab72;
    --accent-orange: #e0775a;
    --front-sky: #d6dfe5;
    --front-mist: #eef2f4;
    --back-deep: #232c38;
    --back-slate: #3a4656;
    --text-light: #ffffff;
  }
  * { margin: 0; padding: 0; box-sizing: border-box; }
  html, body { width: 1200px; height: 1200px; overflow: hidden; background: var(--page); }
  .canvas {
    position: relative; width: 1200px; height: 1200px;
    border: 1px solid var(--frame);
    font-family: "Cabin", "Gill Sans", sans-serif;
  }
  .card { position: absolute; left: 202px; width: 796px; overflow: hidden; }
  .card--front { top: 121px; height: 455px; }
  .card--back { top: 618px; height: 460px; }

  .card__photo { position: absolute; inset: 0; }
  .card--front .card__photo {
    background: linear-gradient(180deg, var(--front-sky) 0%, var(--front-mist) 55%, #ffffff 100%);
  }
  .card--back .card__photo {
    background: radial-gradient(ellipse at 50% 45%, var(--back-slate) 0%, var(--back-deep) 75%);
  }

  .wordmark {
    position: absolute; font-weight: 700; letter-spacing: -2px; line-height: 1;
    display: flex; align-items: center; gap: 12px;
  }
  .wordmark__dot { border-radius: 50%; background: var(--accent-orange); }

  .card--front .wordmark {
    left: 0; right: 0; top: 112px; justify-content: center;
    color: var(--brand-green); font-size: 104px;
  }
  .card--front .wordmark__dot { width: 20px; height: 20px; align-self: flex-end; margin-bottom: 14px; }

  .front-url {
    position: absolute; left: 0; right: 0; top: 392px; text-align: center;
    color: var(--brand-green); font-weight: 700; font-size: 29px;
  }

  .contact { position: absolute; left: 0; right: 0; text-align: center; color: var(--text-light); font-weight: 700; }
  .contact__name { top: 35px; font-size: 58px; }
  .contact__role { top: 108px; font-size: 26px; }
  .contact__phone { top: 144px; font-size: 37px; letter-spacing: 1px; }
  .contact__email { top: 195px; font-size: 25px; }

  .back-url {
    position: absolute; left: 84px; top: 367px;
    color: var(--text-light); font-weight: 700; font-size: 23px;
  }
  .card--back .wordmark {
    right: 42px; top: 340px; color: var(--text-light); font-size: 70px;
  }
</style>
</head>
<body>
<div class="canvas">
  <section class="card card--front">
    <div class="card__photo" role="img" aria-label="Calm water surface with soft ripples under a pale sky"></div>
    <div class="wordmark"><span>brookvane</span><span class="wordmark__dot"></span></div>
    <p class="front-url">www.brookvane.com</p>
  </section>

  <section class="card card--back">
    <div class="card__photo" role="img" aria-label="Water droplets beaded on a dark textured surface"></div>
    <p class="contact contact__name">Mara Ellison</p>
    <p class="contact contact__role">Sales Executive</p>
    <p class="contact contact__phone">+14 15 555 0143</p>
    <p class="contact contact__email">marae@brookvane.com</p>
    <p class="back-url">www.brookvane.com</p>
    <div class="wordmark"><span>brookvane</span></div>
  </section>
</div>
</body>
</html>
```